Magician | Speaker looks for an innovative business card design

I'm a magician and public speaker offering artistic and modern magical experiences.
I'm based in Brussels (Belgium.) I love magic performed up-close, creating a space of intimacy, even when I'm on stage.
The final design should communicate professionalism, elegance, artistry, and a friendly kind personality

I would like to see designs based either on my photos and/or the way I sign my name Theo Varn (see attached files for more info.)
Additional photos and more info about what I offer can be seen at www.theo-varn.net

My current business card design is also attached. I like the fact that the reverse of my current design includes quotes from master magicians about magic, changing the way my participants see the art of magic.

Note: I would like a double-sided card design. However, I need white space on the reverse to be able to write things on for my performances.

Details to include on the card:
Artist name: Theo Varn
Offer: magician + (public) speaker or magic + (public) speaking (the + sign can be replaced by another character, like a bullet or a pipe)
Phone: +32 471 236 519
Email: book@theo-varn.net
(optional) Website: www.theo-varn.net or theo-varn.net

Target Market(s)

Corporate, organisations, companies as well as individuals

Industry/Entity Type

Artists

Colors

Designer to choose colors to be used in the design.

Requirements
Nice to have
• A side with a mirror could be nice

```html
<!DOCTYPE html>
<html lang="en">
<head>
<meta charset="utf-8">
<title>Theo Varn — Magician and Public Speaker Card</title>
<link rel="stylesheet" href="https://fonts.googleapis.com/css2?family=Lato:wght@300;400&family=Nothing+You+Could+Do&display=swap">
<style>
  :root {
    --paper: #ecf2f1;
    --divider: #0a0a0a;
    --violet: #7833fc;
    --lime: #59fd0b;
    --royal: #0b3cfb;
    --crimson: #e80f52;
    --forest: #136747;
    --sky: #add9ef;
    --label-blue: #3a8af5;
    --white: #ffffff;
    --ink: #111111;
    --photo-dark: #1f1a18;
    --photo-warm: #4a2e22;
  }
  * { box-sizing: border-box; margin: 0; padding: 0; }
  html, body { width: 1200px; height: 964px; overflow: hidden; background: var(--paper); }
  .card {
    position: relative; width: 1200px; height: 964px; overflow: hidden;
    background: var(--paper);
    font-family: "Lato", "Helvetica Neue", Arial, sans-serif;
    color: var(--white);
  }
  .divider { position: absolute; left: 579px; top: 0; width: 42px; height: 964px; background: var(--divider); }

  .signature {
    position: absolute; margin: 0;
    font-family: "Nothing You Could Do", cursive;
    font-weight: 400; color: var(--ink); line-height: 1; white-space: nowrap;
  }
  .signature__word { position: absolute; white-space: nowrap; }
  .signature--large { left: 130px; top: 50px; width: 330px; height: 180px; font-size: 84px; }
  .signature--large .signature__first { left: 0; top: 70px; }
  .signature--large .signature__last  { left: 195px; top: 0; }

  .band {
    position: absolute; left: 0; width: 579px; height: 124px;
  }
  .band--phone { top: 257px; background: var(--violet); }
  .band--mail  { top: 390px; background: var(--lime); }
  .band--web   { top: 523px; background: var(--royal); }
  .band--offer { top: 656px; background: var(--crimson); }
  .band--quote { top: 789px; background: var(--forest); }

  .band__icon { position: absolute; left: 62px; top: 50%; transform: translateY(-50%); width: 56px; height: 56px; }
  .band__text {
    position: absolute; left: 155px; right: 20px; top: 50%; transform: translateY(-50%);
    font-size: 24px; font-weight: 400; letter-spacing: 1.4px; line-height: 1.2; white-space: nowrap;
  }
  .band--mail .band__text, .band--web .band__text { left: 158px; }
  .band__text--center { text-align: center; letter-spacing: 0.6px; }
  .band--offer .band__text { left: 120px; right: 114px; font-size: 24px; line-height: 1.5; }
  .band--quote .band__text { left: 125px; right: 66px; font-size: 22.5px; line-height: 1.28; letter-spacing: 0.2px; white-space: normal; }

  .backdrop { position: absolute; left: 913px; top: 24px; width: 255px; height: 458px; background: var(--sky); }
  .photo { position: absolute; }
  .photo--portrait { left: 684px; top: 64px; width: 277px; height: 415px; background: radial-gradient(ellipse at 50% 40%, #3a2a24, var(--photo-dark) 70%); }
  .photo--cards-table { left: 686px; top: 486px; width: 221px; height: 227px; background: linear-gradient(160deg, #3b3a3c, var(--photo-warm)); }
  .photo--coin { left: 915px; top: 486px; width: 221px; height: 227px; background: linear-gradient(160deg, #5c2034, #1c1a1b); }
  .photo--falling-cards { left: 686px; top: 717px; width: 221px; height: 228px; background: linear-gradient(160deg, #263043, #2a201c); }
  .photo--table-reveal { left: 915px; top: 717px; width: 221px; height: 228px; background: linear-gradient(160deg, #6e5a4a, #2b1710); }

  .signature-tile { position: absolute; left: 933px; top: 356px; width: 184px; height: 93px; background: var(--paper); }
  .signature--small { left: 0; top: 0; width: 184px; height: 93px; font-size: 40px; }
  .signature--small .signature__first { left: 12px; top: 36px; }
  .signature--small .signature__last  { left: 104px; top: 4px; }
  .role-label {
    position: absolute; left: 861px; top: 443px; width: 275px; height: 37px;
    background: var(--label-blue); display: flex; align-items: center; justify-content: center;
    font-size: 15.5px; font-weight: 400; letter-spacing: 0.2px; white-space: nowrap;
  }
</style>
</head>
<body>
<main class="card">
  <section class="card-face card-face--contact">
    <h1 class="signature signature--large">
      <span class="signature__word signature__first">Theo</span>
      <span class="signature__word signature__last">Varn</span>
    </h1>

    <div class="band band--phone">
      <svg class="band__icon" viewBox="0 0 56 56" aria-hidden="true">
        <path fill="#fff" d="M15 6c3-2 6-1 7 2l3 9c1 3-1 5-3 6-1 1-1 3 0 5 3 6 6 10 11 13 2 1 3 0 4-1 2-2 4-2 6-1l7 5c2 2 2 4 0 6l-4 4c-4 3-11 1-18-5C19 41 12 30 10 21c-1-6 1-12 5-15z"/>
      </svg>
      <p class="band__text">Phone: +32 471 236 519</p>
    </div>

    <div class="band band--mail">
      <svg class="band__icon" viewBox="0 0 56 56" aria-hidden="true">
        <rect x="1" y="10" width="54" height="37" fill="#fff"/>
        <path d="M3 12 L28 32 L53 12 M3 45 L22 28 M53 45 L34 28" fill="none" stroke="var(--lime)" stroke-width="2.5"/>
      </svg>
      <p class="band__text">book@theo-varn.net</p>
    </div>

    <div class="band band--web">
      <svg class="band__icon" viewBox="0 0 56 56" aria-hidden="true">
        <g fill="none" stroke="#fff" stroke-width="3.5">
          <circle cx="28" cy="28" r="24"/>
          <ellipse cx="28" cy="28" rx="11" ry="24"/>
          <line x1="28" y1="4" x2="28" y2="52"/>
          <line x1="4" y1="28" x2="52" y2="28"/>
          <path d="M8 16 H48 M8 40 H48"/>
        </g>
      </svg>
      <p class="band__text">www.theo-varn.net</p>
    </div>

    <div class="band band--offer">
      <svg class="band__icon" viewBox="0 0 56 56" aria-hidden="true">
        <circle cx="28" cy="28" r="26" fill="#fff"/>
        <circle cx="28" cy="22" r="9" fill="var(--crimson)"/>
        <path d="M12 46 C15 34 41 34 44 46 Z" fill="var(--crimson)"/>
      </svg>
      <p class="band__text band__text--center">magician + (public) speaker,<br>magic + (public) speaking</p>
    </div>

    <div class="band band--quote">
      <svg class="band__icon" viewBox="0 0 56 56" aria-hidden="true">
        <path fill="#fff" d="M2 10h32v20H14l-6 6v-6H2z"/>
        <path fill="#fff" d="M38 16h16v20h-6v6l-6-6H22v-4h16z"/>
      </svg>
      <p class="band__text band__text--center">“The world is full of magic things, patiently waiting for our senses to grow sharper.”</p>
    </div>
  </section>

  <div class="divider"></div>

  <section class="card-face card-face--gallery">
    <div class="backdrop"></div>
    <div class="photo photo--portrait" role="img" aria-label="Portrait of the magician seated in a dark jacket against a brick wall"></div>
    <div class="signature-tile">
      <p class="signature signature--small">
        <span class="signature__word signature__first">Theo</span>
        <span class="signature__word signature__last">Varn</span>
      </p>
    </div>
    <p class="role-label">MAGICIAN AND PUBLIC SPEAKER</p>
    <div class="photo photo--cards-table" role="img" aria-label="Magician fanning playing cards at a wooden table for a guest"></div>
    <div class="photo photo--coin" role="img" aria-label="Hand holding two coins between the fingers"></div>
    <div class="photo photo--falling-cards" role="img" aria-label="Playing cards cascading from one hand into the other"></div>
    <div class="photo photo--table-reveal" role="img" aria-label="Cards and a red rose on a polished round table"></div>
  </section>
</main>
</body>
</html>
```